High End Business Card Design for Flooring Store

Looking for a new card design for our hardwood flooring company. We have no print budget for these and are open to cards made from wood, metal, cardstock with embossed print ... or any combination of these. No plastic.

We sell luxury products and I want the cards to reflect our image of quality and class.

Our contact information as such;
Employee Name
418 Colbrook Blvd.
Fernvale, NB
K9R-3M5
(555) 214-3968
Employee email @velkaflooring.com

Target Market(s)

Home Builders

Contact Information for Business Card

Emnployee name, business contact information

```html
<!DOCTYPE html>
<html lang="en">
<head>
<meta charset="utf-8">
<title>Velka Business Card</title>
<link href="https://fonts.googleapis.com/css2?family=Montserrat:wght@500;600&family=Arimo:wght@400;700&display=swap" rel="stylesheet">
<style>
  :root {
    --brand-red: #932a24;
    --brand-gold: #e9b42a;
    --ink-grey: #6b6b6b;
    --card-white: #ffffff;
    --backdrop: #e7e5e2;
  }
  * { margin: 0; padding: 0; box-sizing: border-box; }
  html, body { width: 1200px; height: 874px; overflow: hidden; }
  body {
    background: var(--backdrop);
    position: relative;
    font-family: "Arimo", Arial, sans-serif;
  }
  .card {
    position: absolute;
    left: 270px;
    width: 660px;
    height: 377px;
    border-radius: 22px;
    overflow: hidden;
    box-shadow: 0 10px 28px rgba(0,0,0,0.18);
  }
  .card--front { top: 40px; background: var(--brand-red); }
  .card--back { top: 457px; background: var(--card-white); }

  .wordmark { position: absolute; display: flex; align-items: center; gap: 12px; }
  .wordmark__square { width: 26px; height: 26px; background: var(--brand-gold); }
  .wordmark__name {
    font-family: "Montserrat", sans-serif;
    font-weight: 500;
    line-height: 1;
    letter-spacing: -1px;
  }
  .tagline {
    position: absolute;
    font-family: "Montserrat", sans-serif;
    font-weight: 500;
    line-height: 1.15;
    text-align: right;
  }

  .card--front .wordmark { left: 120px; top: 100px; }
  .card--front .wordmark__name { font-size: 104px; color: var(--card-white); }
  .card--front .tagline { left: 120px; width: 360px; top: 220px; font-size: 24px; color: var(--card-white); }

  .card--back .wordmark { left: 56px; top: 90px; }
  .card--back .wordmark__square { width: 20px; height: 20px; }
  .card--back .wordmark__name { font-size: 74px; color: var(--brand-red); }
  .card--back .tagline { left: 56px; width: 264px; top: 172px; font-size: 17px; color: var(--ink-grey); }

  .divider {
    position: absolute; left: 340px; top: 76px;
    width: 1.5px; height: 190px; background: #8a8a8a;
  }
  .contact { position: absolute; left: 366px; top: 78px; color: var(--ink-grey); }
  .contact__name { font-size: 22px; font-weight: 700; letter-spacing: 0.5px; }
  .contact__first { color: var(--brand-gold); }
  .contact__last { color: var(--brand-red); }
  .contact__role { font-size: 17px; margin-top: 2px; }
  .contact__address { font-size: 17px; line-height: 1.3; margin-top: 14px; }
  .contact__lines { list-style: none; margin-top: 12px; font-size: 17px; line-height: 1.45; }
  .contact__lines li { display: flex; align-items: center; gap: 8px; }
  .contact__lines svg { width: 15px; height: 15px; flex: none; }
  .contact__domain { color: var(--brand-gold); }

  .swoosh { position: absolute; left: 0; bottom: 0; width: 660px; height: 110px; }
</style>
</head>
<body>
  <section class="card card--front" aria-label="Card front">
    <div class="wordmark">
      <span class="wordmark__square"></span>
      <span class="wordmark__name">Velka</span>
    </div>
    <p class="tagline">Planchers &amp; Escaliers<br>Flooring &amp; Stairs</p>
  </section>

  <section class="card card--back" aria-label="Card back">
    <div class="wordmark">
      <span class="wordmark__square"></span>
      <span class="wordmark__name">Velka</span>
    </div>
    <p class="tagline">Planchers &amp; Escaliers<br>Flooring &amp; Stairs</p>

    <div class="divider"></div>

    <div class="contact">
      <p class="contact__name"><span class="contact__first">MARCUS</span> <span class="contact__last">DELANEY</span></p>
      <p class="contact__role">Manager</p>
      <p class="contact__address">418 Colbrook Blvd.<br>Fernvale, NB, K9R-3M5</p>
      <ul class="contact__lines">
        <li>
          <svg viewBox="0 0 16 16" aria-hidden="true"><path d="M4 1.5l2 3-1.3 1.5a9 9 0 0 0 5.3 5.3L11.5 10l3 2-1 2.5C7 14 2 9 1.5 2.5z" fill="none" stroke="#e9b42a" stroke-width="1.4" stroke-linejoin="round"/></svg>
          (555) 214-3968
        </li>
        <li>
          <svg viewBox="0 0 16 16" aria-hidden="true"><rect x="1.5" y="3.5" width="13" height="9" fill="none" stroke="#e9b42a" stroke-width="1.4"/><path d="M1.5 3.5L8 9l6.5-5.5" fill="none" stroke="#e9b42a" stroke-width="1.4"/></svg>
          info@velkaflooring.com
        </li>
        <li>
          <svg viewBox="0 0 16 16" aria-hidden="true"><circle cx="8" cy="8" r="6.5" fill="none" stroke="#e9b42a" stroke-width="1.3"/><ellipse cx="8" cy="8" rx="2.8" ry="6.5" fill="none" stroke="#e9b42a" stroke-width="1.1"/><path d="M1.5 8h13M2.5 4.8h11M2.5 11.2h11" stroke="#e9b42a" stroke-width="1.1"/></svg>
          <span>www.<span class="contact__domain">velkaflooring</span>.com</span>
        </li>
      </ul>
    </div>

    <svg class="swoosh" viewBox="0 0 660 110" preserveAspectRatio="none" aria-hidden="true">
      <path d="M0 0 C180 62 400 84 660 84 L660 110 L0 110 Z" fill="#932a24"/>
      <path d="M90 24 C260 60 450 68 660 64 L660 72 C450 76 260 64 90 24 Z" fill="#e9b42a"/>
    </svg>
  </section>
</body>
</html>
```